Tarrow Creek plumbing plumbing company business card design

Something sinilar to business card i upload it is my old business card design
And have a good watermark with the logo or majority of the logot in rhe background as watermark

Plumbing business similar to uploaded design with a nice watermark of the logo

Font styles to use
Script

Colors

Designer to choose colors to be used in the design.

```html
<!DOCTYPE html>
<html lang="en">
<head>
<meta charset="utf-8">
<title>Tarrow Creek plumbing – business card</title>
<link rel="stylesheet" href="https://fonts.googleapis.com/css2?family=Montserrat:wght@500;700;800&family=Roboto:wght@400;500&display=swap">
<style>
  :root {
    --bg: #1d1d1f;
    --brand-blue: #1a8fd8;
    --brand-blue-deep: #0f7fc6;
    --card-black: #141414;
    --ink-black: #111111;
    --ink-white: #f4f4f4;
    --watermark-dark: rgba(255,255,255,0.07);
    --watermark-blue: rgba(255,255,255,0.08);
    --rule-blue: #1f86c9;
    --rule-white: #cfcfcf;
  }
  * { box-sizing: border-box; margin: 0; padding: 0; }
  html, body { width: 1200px; height: 1200px; overflow: hidden; }
  body {
    background: radial-gradient(circle at 50% 40%, #2b2b2d 0%, var(--bg) 75%);
    font-family: "Montserrat", sans-serif;
    position: relative;
  }
  .card {
    position: absolute;
    left: 150px;
    width: 900px;
    height: 514px;
    border-radius: 26px;
    overflow: hidden;
    box-shadow: 0 18px 40px rgba(0,0,0,0.55);
  }
  .card--front { top: 52px; background: linear-gradient(135deg, var(--brand-blue-deep), var(--brand-blue)); }
  .card--back { top: 634px; background: var(--card-black); }

  .watermark {
    position: absolute;
    border-radius: 50%;
  }
  .card--front .watermark { width: 520px; height: 520px; right: -120px; top: 40px; background: var(--watermark-blue); }
  .card--back .watermark { width: 440px; height: 440px; right: -90px; top: -40px; background: var(--watermark-dark); }

  .wordmark {
    position: absolute;
    font-weight: 800;
    text-transform: uppercase;
    letter-spacing: 0.04em;
    line-height: 1.05;
  }
  .card--front .wordmark {
    left: 0; right: 0; top: 150px;
    text-align: center;
    font-size: 64px;
    color: var(--ink-black);
  }
  .card--front .website {
    position: absolute; left: 0; right: 0; bottom: 70px;
    text-align: center;
    font-weight: 700; font-size: 19px; letter-spacing: 0.04em;
    color: var(--ink-black);
  }

  .card--back .wordmark {
    left: 70px; top: 62px;
    font-size: 54px;
    color: var(--ink-white);
  }
  .rule { position: absolute; height: 2px; }
  .rule--blue { left: 70px; top: 292px; width: 480px; background: var(--rule-blue); }
  .rule--white { left: 560px; top: 372px; width: 290px; height: 1.5px; background: var(--rule-white); }

  .contacts {
    position: absolute; left: 70px; top: 316px;
    list-style: none;
    font-family: "Roboto", sans-serif;
    font-size: 22px; color: var(--ink-white);
  }
  .contacts li { display: flex; align-items: center; gap: 14px; margin-bottom: 8px; }
  .contacts svg { width: 20px; height: 20px; fill: none; stroke: var(--brand-blue); stroke-width: 2; }

  .person { position: absolute; right: 50px; top: 388px; text-align: right; }
  .person__name { font-weight: 700; font-size: 30px; letter-spacing: 0.06em; color: var(--ink-white); text-transform: uppercase; }
  .person__role { font-weight: 700; font-size: 20px; color: var(--brand-blue); text-transform: uppercase; letter-spacing: 0.03em; }
  .person__licence { font-family: "Roboto", sans-serif; font-size: 20px; color: var(--ink-white); margin-top: 6px; }
  .person__licence span { color: var(--brand-blue); }
</style>
</head>
<body>
  <section class="card card--front">
    <div class="watermark" aria-hidden="true"></div>
    <h1 class="wordmark">Tarrow Creek<br>plumbing</h1>
    <p class="website">TARROWCREEKPLUMBING.COM.AU</p>
  </section>

  <section class="card card--back">
    <div class="watermark" aria-hidden="true"></div>
    <h2 class="wordmark">Tarrow Creek<br>plumbing</h2>
    <div class="rule rule--blue"></div>
    <ul class="contacts">
      <li>
        <svg viewBox="0 0 24 24"><path d="M5 4h4l2 5-3 2a11 11 0 0 0 5 5l2-3 5 2v4a2 2 0 0 1-2 2A17 17 0 0 1 3 6a2 2 0 0 1 2-2z"/></svg>
        0400 000 000
      </li>
      <li>
        <svg viewBox="0 0 24 24"><rect x="3" y="5" width="18" height="14"/><path d="M3 5l9 8 9-8"/></svg>
        info@tarrowcreekplumbing.com.au
      </li>
      <li>
        <svg viewBox="0 0 24 24"><circle cx="12" cy="12" r="9"/><path d="M3 12h18M12 3c3 3 3 15 0 18M12 3c-3 3-3 15 0 18"/></svg>
        tarrowcreekplumbing.com.au
      </li>
    </ul>
    <div class="rule rule--white"></div>
    <div class="person">
      <p class="person__name">Dana Whitlow</p>
      <p class="person__role">Director</p>
      <p class="person__licence"><span>Lic No</span> : 400218c</p>
    </div>
  </section>
</body>
</html>
```